$5 Venture Website Required

I am looking for someone to develop a website akin to the simplicity of www.filecrate.example with a video in the center or a tab that permits one to "Accept the Challenge."

Incorporates our logo and is used to promote our "$5 Venture Program."

Please see attachments, but we are igniting entrepreneurial spirit among our nation's youth through this interactive and intensive program!

There should be a way to navigate to other sections of the site including:

About
Why
Request $5 Venture Packet
Success Stories
Partners
Link to Norvik Holdings
Updates

Thanks to all in advance!

Looking forward to working with you!

Good feel of what we are looking for in terms of "feel"

http://www.brightpathmove.example/

Thank you,

RL

Please make note of this website, we are going for a feel that is akin to this and less modern and professional...more abstract and interactive...but of course include space for our video:

Colors, feel, imagery, is great. Keep your formats, but bring on the feel!

Thank you all for your hard work and patience.

Thank you all for your hard work thus far.

Meanwhile, please understand that the $5 Venture is young, youthful, full of challenge and vitality, it is a competition among students from high school and universities.  The websites you have delivered are too corporate, stale, and standard.  I'm looking for something that is fresh, different, like www.brightpathmove.example.

Symbols, cartoonish, but serious, down to business and save the world one $5 bill at a time.  The logo can be used as a theme...the colors, the feel.

Video space for explanation on the $5 Venture front and center.  With leaves, $ signs, colorful colors, etc.

Visual needs to be compelling to Join the Challenge! Although Norvik Holdings and the tree is a parent company; $5 Venture is separate and Norvik Holdings should only be mentioned as a link.

PixelForum.example in regard to simplicity; and www.brightpathmove.example in terms of style.

Thank you,

Rolando

Like the designs that have been submitted; we are almost there.

Target Market(s)

Professors, students, teachers, parents and NGO leaders who wish to use our program as a way to inspire leadership/entrepreneurship/fundraise for their causes.

Requirements
Must have
• Place for the video, front and center
Include logo
Forsight for blogging, message, etc.
Nice to have
• Plan "buckets" to include"
Explanation Video
Two pamphlets
Contract
FAQs
Website with Blog, voting, registration, video upload, etc.
Flyer perfected
Parable...symbol of our life
Photos
Stats included
Testimonials
Organizations that have used (TMKLU, Birchmoor Lodge, Pellford High)
Sponsors (Open Lens, Marrowind Collegeworks)
Photos from events

I understand this takes coding and such, but want you to be aware of the long term vision for it!

```html
<!DOCTYPE html>
<html lang="en">
<head>
<meta charset="utf-8">
<title>$5 Venture</title>
<link rel="stylesheet" href="https://fonts.googleapis.com/css2?family=Signika:wght@400;600&family=Ubuntu:wght@400;500&display=swap">
<style>
:root{
  --cream:#f6f1de;
  --cream-dark:#ece4c7;
  --green:#3c9a2c;
  --green-dark:#1f7a2a;
  --lime:#b8c61a;
  --olive:#5b6a14;
  --brown:#4a3c22;
  --brown-dark:#2d2414;
  --ink:#555048;
  --grey:#6d6a62;
}
*{box-sizing:border-box;margin:0;padding:0}
html,body{width:948px;height:1200px;overflow:hidden}
body{background:var(--cream);font-family:Arial,Helvetica,sans-serif;color:var(--ink);position:relative}
.abs{position:absolute}

/* header */
.site-header{left:0;top:0;width:948px;height:100px;background:linear-gradient(#f3eedb,#ebe3c8)}
.brand{left:82px;top:20px;font:600 46px/1 Signika,sans-serif;color:#5a5a58}
.parent-link{left:700px;top:12px;font:600 12px Ubuntu,sans-serif;color:#4d4a40;text-decoration:underline}
.main-nav{left:459px;top:63px;display:flex;gap:0;align-items:center}
.main-nav a{font:400 11.5px Ubuntu,sans-serif;color:#4d4a40;text-decoration:none;padding:5px 16px}
.main-nav a.current{background:var(--green-dark);color:#fff;border:1px solid #0d5a18;padding:5px 13px;margin-right:2px}

/* hero */
.hero{left:0;top:100px;width:948px;height:328px;background:radial-gradient(ellipse at 60% 40%,#6a5a36,var(--brown) 55%,var(--brown-dark))}
.hero-photo{left:108px;top:120px;width:262px;height:290px;background:#fff;transform:rotate(5deg);box-shadow:0 3px 8px rgba(0,0,0,.5)}
.hero-photo div{position:absolute;left:10px;top:10px;right:10px;bottom:10px;background:linear-gradient(#6b6f6a,#3b3534 60%,#8b7f88)}
.hero-title{left:415px;top:131px;font:600 29px Signika,sans-serif;color:#fff;text-shadow:0 2px 3px rgba(0,0,0,.6)}
.hero-title span{color:var(--lime)}
.hero-copy{left:415px;top:198px;width:419px;font:400 11px/19.8px Ubuntu,sans-serif;color:#f2ede0;text-align:justify}
.cta{left:421px;top:356px;width:176px;height:39px;border-radius:8px;background:linear-gradient(#8a9b1e,var(--olive));border:2px solid #e6ecc0;color:#fff;font:400 18px/35px Signika,sans-serif;text-align:center;letter-spacing:.5px}
.slide-arrow{top:243px;width:34px;height:75px;background:#f1ecdd;border:1px solid #cfc8b2}

/* columns */
.section-title{font:400 20px Signika,sans-serif;color:var(--green)}
.section-title span{color:var(--lime)}
.badge{width:24px;height:24px;border-radius:50%;background:var(--green)}
.plan-copy{left:85px;top:482px;width:210px;font:400 10px/16.5px Arial,sans-serif;color:#5a564d;text-align:justify;letter-spacing:.3px}
.read-more{left:85px;top:602px;font:400 10.5px Ubuntu,sans-serif;color:var(--green-dark)}
.video{left:363px;top:482px;width:226px;height:130px;border:2px solid #c9c5bd;background:linear-gradient(#a8b7c6,#4a4a4a 55%,#6a6a60)}
.play{left:106px;top:52px;width:30px;height:28px;border-radius:6px;background:rgba(255,255,255,.85)}
.video-bar{left:0;bottom:0;width:100%;height:8px;background:#222}
.pamphlets{left:660px;top:483px;width:195px;height:129px;background:linear-gradient(90deg,#6d8a4a,#f6f0c0 45%,#f0d230 70%,#e27fd2)}
.divider-v{width:0;border-left:2px dashed #e2d9bb}

/* blog + queries */
.blog-panel{left:80px;top:637px;width:788px;height:203px;background:#f8f4e3;border:1px dashed #e3dcc3;border-radius:4px}
.blog-head{font:400 12.5px Ubuntu,sans-serif;color:#55524a}
.blog-copy{width:450px;font:400 10px/17.2px Arial,sans-serif;color:#5a564d;letter-spacing:.3px}
.blog-meta{font:400 11px Arial,sans-serif;color:#55524a}
.tweet{font:400 11px Arial,sans-serif;color:#555;padding:2px 8px 2px 22px;border:1px solid #d5d5d5;border-radius:3px;background:#fff}
.count{width:17px;height:17px;border:1px solid #bbb;border-radius:50%;font:10px/15px Arial;text-align:center;background:#fff}
.field-label{font:400 10.5px Arial,sans-serif;color:#444;text-align:right;width:60px}
.field{width:147px;height:19px;border:1px solid #cfcab0;border-radius:5px;background:#fbfaf3}
.submit{left:757px;top:805px;width:64px;height:19px;border-radius:9px;background:var(--green-dark);color:#fff;font:600 10.5px/19px Arial;text-align:center}

/* events */
.event-photo{top:895px;width:103px;height:103px;background:#fff;border:1px solid #ddd6c4;padding:3px}
.event-photo div{width:100%;height:100%}

/* footer */
.site-footer{left:0;top:1025px;width:948px;height:175px;background:#f1ebd6;border-top:3px double #ddd4bb}
.footer-title{top:1040px;font:600 17px Signika,sans-serif;color:var(--green)}
.footer-links{left:72px;top:1075px;list-style:none;font:400 10.5px/19.8px Arial,sans-serif;color:#55524a;letter-spacing:.4px}
.footer-links li::before{content:"";display:inline-block;border-left:4px solid var(--green);border-top:3px solid transparent;border-bottom:3px solid transparent;margin-right:9px}
.quote{left:271px;top:1075px;width:196px;font:italic 400 10px/16.5px Arial,sans-serif;color:#55524a;text-align:justify}
.sponsor{background:#d9d3c0}
.contact{left:721px;top:1075px;font:400 10px/19.8px Arial,sans-serif;color:#55524a;letter-spacing:.4px}
.social{top:1159px;width:20px;height:20px}
.copyright{left:71px;top:1174px;font:400 10px Arial,sans-serif;color:#55524a}
</style>
</head>
<body>

<header class="site-header abs">
  <div class="brand abs">$5 Venture</div>
  <a class="parent-link abs" href="#">Norvik Holdings</a>
  <nav class="main-nav abs">
    <a class="current" href="#">About</a>
    <a href="#">Why Request $5 Venture Packet</a>
    <a href="#">Success Stories</a>
    <a href="#">Partners</a>
  </nav>
</header>

<section class="hero abs" aria-label="Featured">
</section>
<div class="hero-photo abs" role="img" aria-label="Group photo of program students on steps"><div></div></div>
<h1 class="hero-title abs"><span>A program</span> about people</h1>
<p class="hero-copy abs">Lorem Ipsum is simply dummy text of the printing and typesetting industry. Lorem Ipsum has been the industry's standard dummy text ever since the 1500s, when an unknown printer took a galley of type and scrambled it to make a type specimen book. It has survived not only five centuries, but also the leap into electronic typesetting, remaining essentially unchanged. It was popularised in the 1960s with the release of Letraset sheets</p>
<a class="cta abs" href="#">Accept Challenge</a>
<div class="slide-arrow abs" style="left:0"><svg width="34" height="75"><path d="M22 22 12 37 22 53Z" fill="#b8b09a"/></svg></div>
<div class="slide-arrow abs" style="left:913px"><svg width="34" height="75"><path d="M12 22 22 37 12 53Z" fill="#b8b09a"/></svg></div>

<div class="badge abs" style="left:88px;top:447px"></div>
<h2 class="section-title abs" style="left:122px;top:446px">Plan Buckets</h2>
<p class="plan-copy abs">Lorem Ipsum is simply dummy text of the printing and typesetting industry. Lorem Ipsum has been the industry's standard dummy text ever since the 1500s, when an unknown printer took a galley of type and scrambled it to make a type specimen book. It has survived not only five centuries</p>
<a class="read-more abs" href="#">Read more &#9656;</a>
<div class="divider-v abs" style="left:322px;top:470px;height:140px"></div>

<div class="badge abs" style="left:364px;top:447px"></div>
<h2 class="section-title abs" style="left:398px;top:446px">$5 Venture Video</h2>
<div class="video abs" role="img" aria-label="Program explanation video showing students outdoors">
  <div class="play abs"><svg width="30" height="28"><path d="M11 7 21 14 11 21Z" fill="#333"/></svg></div>
  <div class="video-bar abs"></div>
</div>
<div class="divider-v abs" style="left:624px;top:470px;height:140px"></div>

<div class="badge abs" style="left:648px;top:447px"></div>
<h2 class="section-title abs" style="left:682px;top:446px">See our pamphlets</h2>
<div class="pamphlets abs" role="img" aria-label="Fanned stack of colourful program pamphlets"></div>

<div class="blog-panel abs"></div>
<svg class="abs" style="left:95px;top:632px" width="32" height="46" aria-hidden="true"><path d="M12 4h10l-3 34-3 5-3-5Z" fill="#b8c61a" stroke="#6b7a14"/></svg>
<h2 class="section-title abs" style="left:134px;top:648px;font-size:21px">Latest <span>Blog</span></h2>
<h3 class="blog-head abs" style="left:104px;top:696px">Lorum ipsum is simply a dummy text since 1500</h3>
<p class="blog-copy abs" style="left:104px;top:719px">Lorem Ipsum is simply dummy text of the printing and typesetting industry. Lorem Ipsum has been the industry's standard dummy text ever since the 1500s, when an unknown printer took a galley of type and scrambled it to make a type specimen book. It has survived not only five centuries .</p>
<div class="blog-meta abs" style="left:106px;top:803px">Readmore[+] &nbsp; | &nbsp; 1 comment</div>
<div class="tweet abs" style="left:467px;top:800px">Tweet</div>
<div class="count abs" style="left:534px;top:800px">1</div>
<div class="divider-v abs" style="left:591px;top:648px;height:175px"></div>

<div class="abs" style="left:630px;top:653px;width:25px;height:25px;border-radius:50%;background:var(--green);color:#fff;font:600 15px/25px Signika;text-align:center">?</div>
<h2 class="section-title abs" style="left:667px;top:651px;font-size:21px">Ask <span>Queries</span></h2>
<div class="field-label abs" style="left:602px;top:699px">Name</div>
<div class="field abs" style="left:677px;top:696px"></div>
<div class="field-label abs" style="left:602px;top:727px">Phone</div>
<div class="field abs" style="left:677px;top:724px"></div>
<div class="field-label abs" style="left:602px;top:755px">Query</div>
<div class="field abs" style="left:677px;top:752px;height:41px"></div>
<div class="submit abs">Submit</div>

<svg class="abs" style="left:103px;top:856px" width="26" height="26" aria-hidden="true"><path d="M4 22C6 10 12 6 20 6M14 2l7 4-5 6" fill="none" stroke="#3c9a2c" stroke-width="3"/></svg>
<h2 class="section-title abs" style="left:143px;top:857px;font-size:21px">Our Event <span>Photo's</span></h2>
<div class="event-photo abs" style="left:98px" role="img" aria-label="Exhibition hall event photo"><div style="background:linear-gradient(#4a6ba0,#2c4a82 60%,#3a8fb0)"></div></div>
<div class="event-photo abs" style="left:247px" role="img" aria-label="Crowded evening event photo"><div style="background:linear-gradient(#5a3a2a,#2a1a14 60%,#6a5a3a)"></div></div>
<div class="event-photo abs" style="left:396px" role="img" aria-label="Conference room presentation photo"><div style="background:linear-gradient(#b8a78a,#8a7a62 60%,#d8d0c0)"></div></div>
<div class="event-photo abs" style="left:549px" role="img" aria-label="Speaker at banquet event photo"><div style="background:linear-gradient(#8a2a2a,#b05050 50%,#e8e4e0)"></div></div>
<div class="event-photo abs" style="left:706px" role="img" aria-label="Exhibition hall event photo"><div style="background:linear-gradient(#4a6ba0,#2c4a82 60%,#3a8fb0)"></div></div>

<footer class="site-footer abs"></footer>
<h3 class="footer-title abs" style="left:69px">All Links</h3>
<ul class="footer-links abs">
  <li>About</li><li>Why Request $5 Venture</li><li>Success Stories</li><li>Partners</li>
</ul>
<div class="divider-v abs" style="left:236px;top:1040px;height:115px"></div>
<h3 class="footer-title abs" style="left:270px">Testimonials</h3>
<p class="quote abs">&ldquo; Lorem Ipsum is simply dummy text of the printing and typesetting industry. Lorem Ipsum has been the industry's &rdquo;</p>
<div class="abs" style="left:413px;top:1132px;font:600 10.5px Arial;color:#444">Marlon Teague</div>
<div class="divider-v abs" style="left:487px;top:1040px;height:115px"></div>
<h3 class="footer-title abs" style="left:525px">Our &nbsp;Sponsers</h3>
<div class="sponsor abs" style="left:530px;top:1084px;width:38px;height:12px"></div>
<div class="abs" style="left:575px;top:1073px;width:33px;height:33px;border-radius:50%;background:#9ac43a"></div>
<div class="sponsor abs" style="left:617px;top:1076px;width:20px;height:28px"></div>
<div class="sponsor abs" style="left:530px;top:1124px;width:38px;height:16px"></div>
<div class="abs" style="left:575px;top:1114px;width:33px;height:33px;border-radius:50%;border:2px solid #3a8ac4"></div>
<div class="sponsor abs" style="left:617px;top:1126px;width:24px;height:12px"></div>
<div class="divider-v abs" style="left:690px;top:1040px;height:115px"></div>
<h3 class="footer-title abs" style="left:721px">Contact Us</h3>
<div class="contact abs">$5 venture student program<br>Keldon Rd 6099 Western Australia<br>&nbsp;Ph &nbsp;&nbsp;&nbsp;: &nbsp;&nbsp;(08) 5550 1427<br>&nbsp;Email : &nbsp;&nbsp;info@ventureprogram.example</div>
<div class="abs" style="left:734px;top:1161px;font:600 14px Signika,sans-serif;color:var(--green-dark)">Follow us : -</div>
<div class="social abs" style="left:825px;background:#3b5a9a" aria-label="Social profile one"></div>
<div class="social abs" style="left:856px;background:#4aa8d8" aria-label="Social profile two"></div>
<div class="social abs" style="left:886px;background:#1a6fa8" aria-label="Social profile three"></div>
<div class="copyright abs">Copyright @ &nbsp;$5 venture program.example, All Right Reserved</div>

</body>
</html>
```